Cat-products company needs smart, yet endearing, business card

We need a business card design for a new, but up-and-running, business based in Honolulu, Hawaii. The business is Purrlane Nest Co. Our first product is the most environmentally-friendly cat grass kit ever seen on the planet. Future products, currently in the R&D phase, will include a variety of exciting cat scratchers. We also do consulting work to help apartment-dwellers make their home more cat-friendly and, in the future, plan on doing full, custom installs of structure to create high walkways for cats.

Target Market(s)

Middle-aged, apartment-dwelling, middle-class workers who own 1 or more cats and who dote on them.

Industry/Entity Type

Pet Care

Contact Information for Business Card

A striking, professional, yet warm and friendly design is what we're after.

Font styles to use
Serif
Sans Serif
Other font styles liked:
• Comfortaa

Colors

Designer to choose colors to be used in the design.

Requirements
Must have
• The company logo: (see attachment)
• The company name: Purrlane Nest Co
• The web address: www.purrlanenestco.example
• Email: support@purrlanenestco.example
• Phone: +1 (808) 574 1630
• Update (Fri Jun 30 3017 7:45pm Hawaii Time) I would like, is possible, uploaded picture of the cat grass kit on the back of the card with some text along the lines of: Purrlane Nest Co - Maker Of The Freshest Cat Grass Kit Yet
Nice to have
• A cat picture, cartoon, real or silhouette that illustrates cats in action and/or relaxing; ie using the apartment space to live, play and relax in and being well-contented.
• Most of the website is done in the font: Comfortaa. It might be nice to continue using this for brand consistency.
Should not have
• Hard-to-read fonts.

```html
<!DOCTYPE html>
<html lang="en">
<head>
<meta charset="utf-8">
<title>Purrlane Nest Co – Business Card</title>
<link href="https://fonts.googleapis.com/css2?family=Ubuntu:wght@500;700&family=Open+Sans:wght@400;600&display=swap" rel="stylesheet">
<style>
  :root {
    --page-bg: #3a302b;
    --card-bg: #161616;
    --card-edge: #242424;
    --brand-gold: #f2b21e;
    --brand-brown: #6b3f2f;
    --text-light: #f1f1f1;
    --text-muted: #9a9a9a;
    --divider: #d8d8d8;
    --dot-1: #8a4a3c;
    --dot-2: #3f6a8f;
    --dot-3: #3d7fa6;
    --dot-4: #3a6c8c;
  }
  * { box-sizing: border-box; margin: 0; padding: 0; }
  html, body { width: 1200px; height: 864px; overflow: hidden; }
  body {
    background: var(--page-bg);
    font-family: "Open Sans", Arial, sans-serif;
    position: relative;
  }
  .card {
    position: absolute;
    width: 520px;
    height: 297px;
    background: var(--card-bg);
    border: 1px solid var(--card-edge);
    border-radius: 4px;
    box-shadow: 0 18px 40px rgba(0,0,0,.45);
  }
  .card--front { left: 70px; top: 120px; }
  .card--back  { left: 610px; top: 440px; }

  .brand-mark {
    display: flex;
    align-items: center;
    gap: 10px;
  }
  .brand-mark__square {
    width: 22px; height: 22px;
    background: var(--brand-brown);
    flex: none;
  }
  .brand-mark__name {
    font-family: "Ubuntu", Arial, sans-serif;
    font-weight: 700;
    color: var(--brand-gold);
    line-height: 1.05;
  }

  /* front */
  .card--front .brand-mark { position: absolute; left: 70px; top: 92px; }
  .card--front .brand-mark__name { font-size: 34px; width: 210px; }
  .front__web {
    position: absolute; left: 70px; top: 200px;
    font-size: 13px; letter-spacing: 4px;
    color: var(--text-muted);
  }
  .social-dots {
    position: absolute; right: 26px; top: 28px;
    display: flex; gap: 4px;
  }
  .social-dots span { width: 14px; height: 14px; border-radius: 50%; }
  .social-dots span:nth-child(1) { background: var(--dot-1); }
  .social-dots span:nth-child(2) { background: var(--dot-2); }
  .social-dots span:nth-child(3) { background: var(--dot-3); }
  .social-dots span:nth-child(4) { background: var(--dot-4); }

  /* back */
  .card--back .brand-mark { position: absolute; left: 36px; top: 110px; }
  .card--back .brand-mark__name { font-size: 30px; width: 170px; }
  .back__divider {
    position: absolute; left: 238px; top: 40px;
    width: 1px; height: 220px;
    background: linear-gradient(to bottom, transparent, var(--divider) 30%, var(--divider) 70%, transparent);
  }
  .contact { position: absolute; left: 262px; top: 78px; color: var(--text-light); }
  .contact__name {
    font-family: "Ubuntu", Arial, sans-serif;
    font-weight: 500; font-size: 13px;
    color: var(--brand-brown); text-transform: uppercase;
  }
  .contact__role {
    font-family: "Ubuntu", Arial, sans-serif;
    font-size: 14px; color: var(--brand-gold);
    margin-bottom: 12px;
  }
  .contact__address { font-size: 13px; line-height: 1.4; margin-bottom: 4px; }
  .contact__line {
    display: flex; align-items: center; gap: 8px;
    font-size: 13px; line-height: 1.55;
  }
  .contact__line svg { width: 11px; height: 11px; flex: none; fill: var(--brand-brown); }
</style>
</head>
<body>

<section class="card card--front" aria-label="Card front">
  <div class="social-dots" aria-hidden="true"><span></span><span></span><span></span><span></span></div>
  <div class="brand-mark">
    <span class="brand-mark__square"></span>
    <span class="brand-mark__name">Purrlane Nest Co</span>
  </div>
  <p class="front__web">www.purrlanenestco.example</p>
</section>

<section class="card card--back" aria-label="Card back">
  <div class="brand-mark">
    <span class="brand-mark__square"></span>
    <span class="brand-mark__name">Purrlane Nest Co</span>
  </div>
  <div class="back__divider"></div>
  <div class="contact">
    <p class="contact__name">Leilani Kahale</p>
    <p class="contact__role">CEO/FOUNDER</p>
    <p class="contact__address">1420 Mango Grove Way<br>Honolulu, Hawaii 96815</p>
    <p class="contact__line">
      <svg viewBox="0 0 12 12" aria-hidden="true"><path d="M2.5 0.5l2 2.2-1 1.4c.7 1.6 1.8 2.7 3.4 3.4l1.4-1 2.2 2-1 2.5C5.3 11 1 6.7.9 1.5z"/></svg>
      +1 (808) 574 1630
    </p>
    <p class="contact__line">
      <svg viewBox="0 0 12 12" aria-hidden="true"><path d="M0 2h12v8H0z M0 2l6 4 6-4" /></svg>
      support@purrlanenestco.example
    </p>
    <p class="contact__line">
      <svg viewBox="0 0 12 12" aria-hidden="true"><circle cx="6" cy="6" r="6"/></svg>
      www.purrlanenestco.example
    </p>
  </div>
</section>

</body>
</html>
```